Lantern Advisory Website

I currently have a website www.lanternadvisoryinc.example. We are a IT Consulting Company. Our website will pretty much tell out our services. I am looking to enhance my website and make it look more professional. Looking for very classy and Contemporary look and design for my website.

It Company

```html
<!DOCTYPE html>
<html lang="en">
<head>
<meta charset="utf-8">
<title>Lantern Advisory</title>
<link rel="stylesheet" href="https://fonts.googleapis.com/css2?family=Source+Sans+3:wght@400;600;700&display=swap">
<style>
:root{
  --purple:#3b2a6b;
  --blue:#1463a8;
  --cyan:#0a98d2;
  --nav:#cfe2ee;
  --nav-active:#29a3d8;
  --drop:#c9c9cc;
  --panel:#ececec;
  --text:#222;
  --muted:#555;
  --footer:#6a6665;
  --footer-dark:#4b4847;
  --page:#f6f6f7;
}
*{box-sizing:border-box;margin:0;padding:0}
html,body{width:898px;height:1200px;overflow:hidden}
body{position:relative;background:#fff;font-family:"Source Sans 3",sans-serif;color:var(--text)}
.abs{position:absolute}
.top-strip{left:0;top:0;width:898px;height:7px;background:#d6d6da}
.header-band{left:0;top:7px;width:898px;height:374px;background:linear-gradient(#fbfbfc,#eeeef0)}
.brand{left:135px;top:24px;display:flex;align-items:center;gap:8px}
.brand-mark{width:34px;height:34px;border-radius:50%;background:var(--blue)}
.brand-name{font-size:19px;font-weight:700;color:var(--blue);letter-spacing:.2px}
.partner-badge{left:392px;top:18px;width:108px;height:30px;border-radius:3px;background:#dcdce0}
.divider{width:1px;height:50px;background:#c8c8cc;top:8px}
.follow-label{font-size:11px;color:var(--muted)}
.social{width:24px;height:24px;border-radius:50%;background:#cfcfd3}
.search-box{left:636px;top:38px;width:128px;height:21px;border:1px solid #b8a8d8;background:#fff}
.nav{left:0;top:88px;width:898px;height:26px;background:#e6e6e8}
.nav-list{left:127px;top:88px;width:645px;height:26px;display:flex;list-style:none}
.nav-list li{flex:1;background:var(--nav);border-right:1px solid #fff;font-size:12px;color:#333;display:flex;align-items:center;justify-content:center}
.nav-list li.active{background:var(--nav-active);color:#fff}
.dropdown{left:127px;top:114px;width:107px;list-style:none;z-index:3}
.dropdown li{height:25px;background:var(--drop);border-bottom:1px solid #e4e4e4;font-size:12px;color:#333;display:flex;align-items:center;justify-content:center}
.hero{left:127px;top:114px;width:645px;height:267px;background:#f3f3f4;overflow:hidden}
.hero-photo{position:absolute;left:205px;top:0;width:440px;height:267px;background:linear-gradient(90deg,rgba(243,243,244,1) 0%,#c9c6c4 25%,#8d8a88 55%,#b7b2ad 100%)}
.hero-title{position:absolute;left:27px;top:100px;font-size:22px;line-height:26px;color:var(--purple)}
.hero-caption{position:absolute;left:0;bottom:0;width:100%;height:34px;background:rgba(80,80,80,.85);color:#fff;font-size:12px;padding-left:34px;display:flex;align-items:center}
.hero-shadow{left:160px;top:380px;width:580px;height:14px;border-radius:50%;background:radial-gradient(ellipse at center,rgba(0,0,0,.28),rgba(0,0,0,0) 70%)}
.dot{width:12px;height:12px;border-radius:50%;top:406px;background:var(--purple)}
.dot.light{background:#a59cc4}
.intro-title{left:0;top:445px;width:898px;text-align:center;font-size:22px;font-weight:600;color:var(--purple)}
.intro-text{left:139px;top:478px;width:620px;text-align:center;font-size:13px;line-height:15.5px;font-weight:600;color:#333}
.feature-icon{width:98px;height:98px;border-radius:50%;background:var(--blue);top:556px;display:flex;align-items:center;justify-content:center}
.feature-label{top:660px;width:180px;text-align:center;font-size:20px;font-weight:600;color:#333}
.panels{left:128px;top:711px;width:643px;height:151px;background:var(--panel);display:flex}
.panel{flex:1;border-right:1px solid #c9c9d6;padding:9px 6px 0;position:relative}
.panel:last-child{border-right:none}
.panel p{font-size:10px;line-height:12px;text-align:center;color:#222;padding:0 8px}
.btn{position:absolute;left:6px;right:6px;top:98px;height:33px;border-radius:3px;background:var(--cyan);color:#fff;font-size:12px;display:flex;align-items:center;justify-content:center}
.quote-mark{left:142px;top:885px}
.section-title{font-size:20px;color:#222}
.section-title small{font-size:13px}
.body-copy{font-size:10px;line-height:12px;color:#222}
.read-more{font-size:12px;color:var(--purple)}
.news-image{left:464px;top:932px;width:133px;height:88px;background:linear-gradient(135deg,#c9d4df,#e9e7e3 55%,#9fb2c4)}
.footer-strip{left:0;top:1064px;width:898px;height:14px;background:var(--footer-dark)}
.footer{left:0;top:1078px;width:898px;height:122px;background:var(--footer)}
.footer-brand{left:160px;top:1094px;display:flex;align-items:center;gap:6px}
.footer-brand .brand-mark{width:26px;height:26px;background:#fff}
.footer-brand .brand-name{font-size:13px;color:#fff}
.footer-links{list-style:none;font-size:9.5px;line-height:11.2px;color:#fff}
.footer-text{font-size:10px;color:#fff}
.footer .social{background:#e6e6e6}
</style>
</head>
<body>
<div class="abs top-strip"></div>
<div class="abs header-band"></div>

<header>
  <div class="abs brand"><span class="brand-mark"></span><span class="brand-name">Lantern Advisory</span></div>
  <div class="abs partner-badge" role="img" aria-label="Corvane partner badge"></div>
  <div class="abs divider" style="left:513px"></div>
  <div class="abs follow-label" style="left:522px;top:18px">Follow Brightfold</div>
  <span class="abs social" style="left:522px;top:34px"></span>
  <span class="abs social" style="left:552px;top:34px"></span>
  <div class="abs divider" style="left:624px"></div>
  <div class="abs follow-label" style="left:636px;top:18px">Search here</div>
  <div class="abs search-box"></div>
</header>

<nav>
  <div class="abs nav"></div>
  <ul class="abs nav-list">
    <li class="active">About Us</li><li>Services</li><li>Solutions</li><li>Resource</li><li>Career</li><li>Contact Us</li>
  </ul>
  <ul class="abs dropdown"><li>History</li><li>Our Values</li></ul>
</nav>

<section class="abs hero">
  <div class="hero-photo" role="img" aria-label="Business team meeting around a conference table"></div>
  <h1 class="hero-title" style="font-weight:400">Today’s<br>IT market is a<br>dynamic,<br>fast-paced industry</h1>
  <div class="hero-caption">Insurance: Another Corvane Gold Competency for meridian4....</div>
</section>
<div class="abs hero-shadow"></div>
<span class="abs dot" style="left:451px"></span>
<span class="abs dot" style="left:473px"></span>
<span class="abs dot light" style="left:494px"></span>

<section>
  <h2 class="abs intro-title">LANTERN ADVISORY MAINTAINS A GLOBAL PRESENCE</h2>
  <p class="abs intro-text">aggressively recruiting expertly qualified IT and Management Professionals from around the world and cultivating key partnerships with corporations to understand their business models end-to-end, with a goal of delivering exceptional client service and ensuring a consistent delivery of the talent needed to drive results.</p>
</section>

<section class="features">
  <div class="abs feature-icon" style="left:167px">
    <svg width="44" height="44" viewBox="0 0 44 44" fill="#fff"><g transform="translate(22 22)"><rect x="-4" y="-21" width="8" height="42" rx="1"/><rect x="-4" y="-21" width="8" height="42" rx="1" transform="rotate(45)"/><rect x="-4" y="-21" width="8" height="42" rx="1" transform="rotate(90)"/><rect x="-4" y="-21" width="8" height="42" rx="1" transform="rotate(135)"/><circle r="15"/><circle r="6" fill="#1463a8"/></g></svg>
  </div>
  <div class="abs feature-icon" style="left:324px">
    <svg width="48" height="40" viewBox="0 0 48 40" fill="#fff"><path d="M17 8V5a3 3 0 0 1 3-3h8a3 3 0 0 1 3 3v3h-3V5h-8v3z"/><rect x="1" y="8" width="46" height="30" rx="5"/></svg>
  </div>
  <div class="abs feature-icon" style="left:480px">
    <svg width="50" height="38" viewBox="0 0 50 38" fill="none" stroke="#fff" stroke-width="3"><rect x="7" y="3" width="36" height="25" rx="1"/><path d="M2 32h46v3H2z" fill="#fff"/></svg>
  </div>
  <div class="abs feature-icon" style="left:635px">
    <svg width="40" height="46" viewBox="0 0 40 46" fill="#fff"><circle cx="20" cy="15" r="10"/><path d="M8 15a12 12 0 0 1 24 0" fill="none" stroke="#fff" stroke-width="3"/><path d="M4 46c0-12 7-17 16-17s16 5 16 17z"/></svg>
  </div>
  <div class="abs feature-label" style="left:124px">Services</div>
  <div class="abs feature-label" style="left:285px">Solustions</div>
  <div class="abs feature-label" style="left:437px">Offshore</div>
  <div class="abs feature-label" style="left:598px">Consulting</div>

  <div class="abs panels">
    <div class="panel"><p>Lantern Advisory has certified professional consultants to work with you to help increase the business by providing IT services ...</p><span class="btn">Read More</span></div>
    <div class="panel"><p>Lantern Advisory has certified professional consultants to work with you to help increase the business by providing IT services ...</p><span class="btn">Read More</span></div>
    <div class="panel"><p>Lantern Advisory has certified professional consultants to work with you to help increase the business by providing IT services ...</p><span class="btn">Read More</span></div>
    <div class="panel"><p>Lantern Advisory has certified professional consultants to work with you to help increase the business by providing IT services ...</p><span class="btn">Read More</span></div>
  </div>
</section>

<section class="testimonials">
  <svg class="abs quote-mark" width="38" height="46" viewBox="0 0 38 46" fill="#dcdcdc"><path d="M2 44V24C2 12 6 5 14 2l2 4c-5 3-7 8-7 14h7v24zM22 44V24c0-12 4-19 12-22l2 4c-5 3-7 8-7 14h7v24z"/></svg>
  <h3 class="abs section-title" style="left:187px;top:896px;font-weight:600">What <small>Client Say about us</small></h3>
  <p class="abs body-copy" style="left:146px;top:946px;width:250px">Lantern Advisory has certified professional consultants to work with you to help increase the business by providing IT services ...</p>
  <span class="abs read-more" style="left:147px;top:1014px">Read More</span>
</section>

<section class="news">
  <h3 class="abs section-title" style="left:464px;top:893px;font-weight:600">Latest <small>news &amp; events</small></h3>
  <div class="abs news-image" role="img" aria-label="Calculator resting on a financial spreadsheet"></div>
  <p class="abs body-copy" style="left:618px;top:931px;width:140px">Lantern Advisory has certified professional consultants to work with you to help increase the business by providing IT services ...</p>
  <span class="abs read-more" style="left:618px;top:1014px">Read More</span>
</section>

<div class="abs footer-strip"></div>
<footer class="abs footer"></footer>
<div class="abs footer-brand"><span class="brand-mark"></span><span class="brand-name">Lantern Advisory</span></div>
<div class="abs footer-text" style="left:167px;top:1132px">Copyright © 2016</div>
<ul class="abs footer-links" style="left:305px;top:1094px"><li>Home</li><li>About Us</li><li>Partners</li><li>Testimonial</li><li>Clients</li><li>Management Team</li><li>Contact Us</li></ul>
<ul class="abs footer-links" style="left:419px;top:1095px"><li>Blog</li><li>Updated News</li><li>Site Map</li><li>Privacy Policy</li><li>Cookie Policy</li></ul>
<div class="abs footer-text" style="left:618px;top:1094px;font-size:11px">Follow Brightfold</div>
<span class="abs social" style="left:618px;top:1116px;background:#e6e6e6"></span>
<span class="abs social" style="left:648px;top:1116px;background:#e6e6e6"></span>
</body>
</html>
```